Would like a Northwest feel to the look, something NOT typical of what you would see on a typical Home Inspectors logo. Real estate cards all the same as well, and would like to stand out. Earthy, green, Northwest. Sadly a portrait seems to be a requirement (see the attached). I inspect residential homes for buyers and sellers.

Target Market(s)

Home Buyers and Sellers

Industry/Entity Type

Home Inspection

Contact Information for Business Card

See description
Note: The name Corvaneth is a Chinook word that means 'Friend'. Please do not associate the name with the Whale that shows up on 99% of google searches.

Logo Text

Corvaneth Home Inspections

Colors

Designer to choose colors to be used in the design.

Requirements
Must have
• Phone Num: 541-672-8153
• Address: 732 SW 219th Av Num 618
• Portland, Oregon 97388
• Email: glen@corvanethhomeinspection.example
• Website: www.CorvanethHomeInspection.example
• Additional Note: Need to add the Obravex logo (icon). It should be small and not the focus of the card. The logo can be found at Obravex.example
Nice to have
• I am open
Should not have
• Cant think of anything

```html
<!DOCTYPE html>
<html lang="en">
<head>
<meta charset="utf-8">
<title>Corvaneth Home Inspections – Business Card</title>
<link rel="stylesheet" href="https://fonts.googleapis.com/css2?family=Lato:wght@400;700;900&display=swap">
<style>
  :root {
    --forest: #2b4222;
    --lime: #a4be30;
    --leaf: #7aaa33;
    --white: #ffffff;
    --canvas: #ffffff;
    --photo-dark: #4a2410;
    --photo-warm: #d98a24;
  }
  * { margin: 0; padding: 0; box-sizing: border-box; }
  html, body {
    width: 1200px; height: 1200px; overflow: hidden;
    background: var(--canvas);
    font-family: 'Lato', sans-serif;
  }
  .card {
    position: absolute; left: 181px; width: 840px; height: 480px;
    background: var(--forest); overflow: hidden;
  }
  .card--front { top: 114px; }
  .card--back { top: 618px; }

  .portrait {
    position: absolute; left: 61px; top: 30px; width: 215px; height: 290px;
    background: radial-gradient(circle at 85% 70%, var(--photo-warm), var(--photo-dark) 70%);
  }
  .accent-bar {
    position: absolute; left: 316px; top: 0; width: 60px; height: 398px;
    background: var(--lime); border-radius: 0 0 30px 30px;
  }
  .brand {
    position: absolute; display: flex; align-items: center; color: var(--leaf);
    font-weight: 900;
  }
  .brand__dot { border-radius: 50%; background: var(--leaf); flex: none; }
  .brand__name { line-height: 1.05; }
  .brand--small { left: 52px; top: 366px; gap: 12px; }
  .brand--small .brand__dot { width: 60px; height: 60px; }
  .brand--small .brand__name { font-size: 24px; }

  .identity { position: absolute; left: 461px; top: 26px; }
  .identity__name { color: var(--white); font-size: 46px; font-weight: 400; line-height: 1.1; }
  .identity__role { color: var(--lime); font-size: 19px; margin-top: 4px; }
  .identity__cert { color: var(--lime); font-size: 19px; margin-top: 18px; line-height: 1.2; }
  .identity__cert-number { font-size: 16px; padding-left: 4px; }

  .contact { position: absolute; left: 401px; list-style: none; }
  .contact li { position: absolute; left: 0; display: flex; align-items: center; white-space: nowrap; }
  .contact li:nth-child(1) { top: 197px; }
  .contact li:nth-child(2) { top: 248px; }
  .contact li:nth-child(3) { top: 300px; }
  .contact__icon {
    width: 40px; height: 40px; border-radius: 50%; background: var(--white);
    display: flex; align-items: center; justify-content: center; margin-right: 20px;
  }
  .contact__text { color: var(--white); font-size: 19px; letter-spacing: 0.5px; }

  .address {
    position: absolute; left: 421px; top: 362px;
    color: var(--white); font-size: 19px; line-height: 24px; font-style: normal;
  }

  .brand--large { left: 195px; top: 140px; gap: 22px; }
  .brand--large .brand__dot { width: 140px; height: 140px; }
  .brand--large .brand__name { font-size: 46px; }
  .back-band {
    position: absolute; left: 0; bottom: 0; width: 100%; height: 62px;
    background: var(--lime); display: flex; align-items: center; justify-content: center;
    color: var(--forest); font-size: 18px; letter-spacing: 0.5px;
  }
</style>
</head>
<body>
  <section class="card card--front">
    <div class="portrait" role="img" aria-label="Portrait photograph of the home inspector"></div>
    <div class="accent-bar"></div>
    <div class="brand brand--small">
      <span class="brand__dot"></span>
      <span class="brand__name">Corvaneth<br>Home Inspections</span>
    </div>

    <div class="identity">
      <h1 class="identity__name">Glen Hadley</h1>
      <p class="identity__role">Home inspector</p>
      <p class="identity__cert">Certificate number<br><span class="identity__cert-number">XXXX-XXXXX-XXXXXX</span></p>
    </div>

    <ul class="contact">
      <li>
        <span class="contact__icon">
          <svg width="24" height="24" viewBox="0 0 24 24"><path fill="#7aaa33" d="M6.6 10.8a15 15 0 0 0 6.6 6.6l2.2-2.2c.3-.3.7-.4 1-.2 1.1.4 2.3.6 3.6.6.6 0 1 .4 1 1V20c0 .6-.4 1-1 1A17 17 0 0 1 3 4c0-.6.4-1 1-1h3.5c.6 0 1 .4 1 1 0 1.3.2 2.5.6 3.6.1.3 0 .7-.2 1z"/></svg>
        </span>
        <span class="contact__text">541-672-8153</span>
      </li>
      <li>
        <span class="contact__icon">
          <svg width="26" height="22" viewBox="0 0 26 22"><g fill="none" stroke="#7aaa33" stroke-width="1.6"><path d="M2 9 13 2l11 7v11H2z"/><path d="M2 9l11 7 11-7M2 20l8-6M24 20l-8-6"/></g></svg>
        </span>
        <span class="contact__text">glen@corvanethhomeinspection.example</span>
      </li>
      <li>
        <span class="contact__icon">
          <svg width="26" height="26" viewBox="0 0 26 26"><g fill="none" stroke="#7aaa33" stroke-width="1.6"><circle cx="13" cy="13" r="11"/><ellipse cx="13" cy="13" rx="5" ry="11"/><path d="M2 13h22M4 7h18M4 19h18M13 2v22"/></g></svg>
        </span>
        <span class="contact__text">www.CorvanethHomeInspection.example</span>
      </li>
    </ul>

    <address class="address">732 SW 219th Av Num 618<br>Portland, Oregon 97388</address>
  </section>

  <section class="card card--back">
    <div class="brand brand--large">
      <span class="brand__dot"></span>
      <span class="brand__name">CORVANETH<br>Home Inspections</span>
    </div>
    <div class="back-band">www.CorvanethHomeInspection.example</div>
  </section>
</body>
</html>
```